Health care technology software systems

We have a solid logo. We have company colors that will need to be used as well. We just need a great business card design. We sell to health plans but want to be modern
Updates

Need extra days to review

Target Market(s)

Health technology sector selling into Health Plans

Industry/Entity Type

Health Care Technology

Contact Information for Business Card

Name, title, address, phone number, email

Requirements
Must have
• Use of Kembrata corporate colors - Uploaded w/ our logos

```html
<!DOCTYPE html>
<html lang="en">
<head>
<meta charset="utf-8">
<title>Kembrata Business Card</title>
<link href="https://fonts.googleapis.com/css2?family=Roboto:wght@300;400;500&display=swap" rel="stylesheet">
<style>
  :root {
    --backdrop: #ededed;
    --card: #ffffff;
    --brand-blue: #1a67a3;
    --brand-sky: #12a3dc;
    --ink: #3a3f42;
    --shadow: rgba(0, 0, 0, 0.45);
  }
  * { margin: 0; padding: 0; box-sizing: border-box; }
  html, body {
    width: 1200px;
    height: 1200px;
    overflow: hidden;
    background: var(--backdrop);
    font-family: "Roboto", Arial, sans-serif;
    color: var(--ink);
  }
  .canvas { position: relative; width: 1200px; height: 1200px; }
  .card {
    position: absolute;
    left: 280px;
    width: 640px;
    height: 365px;
    background: var(--card);
    border-radius: 22px;
    box-shadow: 6px 8px 10px var(--shadow);
  }
  .card--front { top: 190px; }
  .card--back { top: 643px; }

  .wordmark {
    position: absolute;
    display: flex;
    align-items: center;
    font-weight: 300;
    color: var(--ink);
    letter-spacing: 1px;
    line-height: 1;
  }
  .wordmark__dot {
    border-radius: 50%;
    background: var(--brand-blue);
    flex: none;
  }
  .card--front .wordmark { left: 156px; top: 68px; font-size: 58px; gap: 24px; }
  .card--front .wordmark__dot { width: 60px; height: 60px; }
  .card--back .wordmark { left: 115px; top: 144px; font-size: 76px; gap: 30px; }
  .card--back .wordmark__dot { width: 76px; height: 76px; }

  .holder {
    position: absolute;
    left: 0; right: 0;
    top: 186px;
    text-align: center;
  }
  .holder__name {
    font-weight: 500;
    font-size: 24px;
    color: var(--brand-blue);
    line-height: 30px;
  }
  .holder__title {
    font-size: 19px;
    line-height: 24px;
  }
  .divider {
    position: absolute;
    left: 27px; right: 27px;
    top: 250px;
    height: 3px;
    background: var(--brand-blue);
  }
  .address {
    position: absolute;
    left: 36px;
    top: 290px;
    font-size: 17px;
    line-height: 19px;
  }
  .contacts {
    position: absolute;
    left: 436px;
    top: 284px;
    list-style: none;
    font-size: 17px;
  }
  .contacts li {
    display: flex;
    align-items: center;
    gap: 7px;
    height: 21px;
    margin-bottom: 8px;
  }
  .contacts svg { width: 14px; height: 14px; fill: var(--brand-blue); }
</style>
</head>
<body>
<main class="canvas">
  <section class="card card--front">
    <div class="wordmark"><span class="wordmark__dot"></span><span>kembrata</span></div>
    <div class="holder">
      <p class="holder__name">LOREM LPSUM</p>
      <p class="holder__title">Founder</p>
    </div>
    <div class="divider"></div>
    <address class="address" style="font-style: normal;">
      123, Dummy Road, Lorem ipsum,<br>County, DR 12345
    </address>
    <ul class="contacts">
      <li>
        <svg viewBox="0 0 24 24" aria-hidden="true"><path d="M6.6 10.8c1.4 2.8 3.8 5.1 6.6 6.6l2.2-2.2c.3-.3.7-.4 1-.2 1.1.4 2.3.6 3.6.6.6 0 1 .4 1 1V20c0 .6-.4 1-1 1C10.6 21 3 13.4 3 4c0-.6.4-1 1-1h3.5c.6 0 1 .4 1 1 0 1.3.2 2.5.6 3.6.1.3 0 .7-.2 1l-2.3 2.2z"/></svg>
        <span>(000) 123-4567</span>
      </li>
      <li>
        <svg viewBox="0 0 24 24" aria-hidden="true"><path d="M2 5h20v14H2z M3.5 6.5 12 13l8.5-6.5" fill="var(--brand-blue)" stroke="#fff" stroke-width="1.5"/></svg>
        <span>info@kembrata.com</span>
      </li>
    </ul>
  </section>

  <section class="card card--back">
    <div class="wordmark"><span class="wordmark__dot"></span><span>kembrata</span></div>
  </section>
</main>
</body>
</html>
```